Shop Window Desgin

I have a big glass window (office), 280cm wide by 302cm high and I want designing an advert for our property management business.

Our main colours are in the proeprty management logo attached. I have also uploaded a photo of the shop front (left window), please take into consideration the door.

I want the following text items placed:

PROPERTY MANAGEMENT
HOLIDAY RENTALS
KEYHOLDING
MARKETING & RESERVATIONS
GARDEN & POOL MAINTENACE
CLEANING & LAUNDRY

```html
<!DOCTYPE html>
<html lang="en">
<head>
<meta charset="utf-8">
<title>Property Services Window Advert</title>
<link rel="stylesheet" href="https://fonts.googleapis.com/css2?family=Oswald:wght@500&display=swap">
<style>
  :root {
    --stage: #808080;
    --paper-top: #ffffff;
    --paper-bottom: #fcfae6;
    --orange: #e98127;
    --text-grey: #7b7b7b;
    --rule-grey: #9a9a9a;
    --house-grey: #8a8a8a;
  }
  * { margin: 0; padding: 0; box-sizing: border-box; }
  html, body {
    width: 1200px; height: 1091px; overflow: hidden;
    background: var(--stage);
  }
  .window-advert {
    position: absolute; left: 271px; top: 193px;
    width: 657px; height: 705px;
    background: linear-gradient(to bottom, var(--paper-top) 0%, var(--paper-bottom) 100%);
    overflow: hidden;
  }
  .rule-h, .rule-v { position: absolute; }
  .rule-h { left: 65px; width: 525px; border-top: 1px dashed var(--rule-grey); }
  .rule-v { left: 343px; top: 40px; height: 510px; border-left: 1px dashed var(--rule-grey); }
  .service-icon {
    position: absolute; width: 86px; height: 86px; margin: -43px 0 0 -43px;
    border-radius: 50%; background: #fff;
    box-shadow: 1px 2px 4px rgba(0,0,0,0.18);
  }
  .service-icon::after {
    content: ""; position: absolute; left: 5px; top: 5px;
    width: 76px; height: 76px; border-radius: 50%; background: var(--orange);
  }
  .service-title {
    position: absolute; width: 320px; margin-left: -160px;
    text-align: center;
    font-family: "Oswald", "Arial Narrow", sans-serif;
    font-weight: 500; font-size: 30px; line-height: 40px;
    color: var(--text-grey); transform: scaleX(0.92);
    text-transform: uppercase; letter-spacing: 0;
  }
  .street-scene {
    position: absolute; left: 0; top: 592px; width: 657px; height: 86px;
    background: linear-gradient(to bottom, rgba(233,129,39,0) 0%, rgba(233,129,39,0.55) 35%, var(--orange) 70%, var(--house-grey) 100%);
  }
  .ground-band {
    position: absolute; left: 0; top: 678px; width: 657px; height: 27px;
    background: var(--orange);
  }
</style>
</head>
<body>
  <main class="window-advert">
    <div class="rule-v"></div>
    <div class="rule-h" style="top:189px"></div>
    <div class="rule-h" style="top:360px"></div>

    <div class="service-icon" role="img" aria-label="Hand holding buildings and money bag icon" style="left:179px;top:74px"></div>
    <h2 class="service-title" style="left:179px;top:129px">Property Management</h2>

    <div class="service-icon" role="img" aria-label="Palm tree and sun on the beach icon" style="left:481px;top:74px"></div>
    <h2 class="service-title" style="left:481px;top:129px">Holiday Rentals</h2>

    <div class="service-icon" role="img" aria-label="Bucket, mop and bubbles icon" style="left:179px;top:246px"></div>
    <h2 class="service-title" style="left:179px;top:301px">Cleaning &amp; Laundry</h2>

    <div class="service-icon" role="img" aria-label="Key over an open hand icon" style="left:481px;top:246px"></div>
    <h2 class="service-title" style="left:481px;top:301px">Keyholding</h2>

    <div class="service-icon" role="img" aria-label="Pool ladder over water icon" style="left:179px;top:418px"></div>
    <h2 class="service-title" style="left:179px;top:473px">Garden &amp; Pool<br>Maintenace</h2>

    <div class="service-icon" role="img" aria-label="Hand tapping a phone booking screen icon" style="left:481px;top:418px"></div>
    <h2 class="service-title" style="left:481px;top:473px">Marketing &amp;<br>Reservations</h2>

    <div class="street-scene" role="img" aria-label="Illustrated row of orange houses and apartment blocks with trees"></div>
    <div class="ground-band"></div>
  </main>
</body>
</html>
```